Business card for different employees

A professional new updated design incorporating our current business's color themes and styles such as our on-site service trucks decals included in pictures attached. Our current business card is very simple and not professionally designed. We are a small family business but want a professional corporate look.

Target Market(s)

Cards to be handed out to new customers , corperate meetings. For our on site service operators.

Industry/Entity Type

Hydraulic

Contact Information for Business Card

Address, website, phone number, email, logo.
slogan - "Industry chosen hose and fittings provider".
24/7 on-site service , supply and hose management
Experienced , indpendant , family owned

Font styles to use
Sans Serif

Requirements
Must have
• Easily editable so that I can add different names and different roles for employees etc.
Nice to have
• Freedom with colour doesn't necessarily have to be blue but that is our company colour theme with trucks and logo so makes sense for the card to have blue like the trucks.

```html
<!DOCTYPE html>
<html lang="en">
<head>
<meta charset="utf-8">
<title>Meridian Hose and Fittings – Business Card</title>
<link rel="stylesheet" href="https://fonts.googleapis.com/css2?family=Exo+2:wght@500;700;800&family=Poppins:wght@400;500&display=swap">
<style>
  :root {
    --paper: #e4e4e4;
    --white: #ffffff;
    --navy-deep: #141a66;
    --navy: #1c2490;
    --brand-blue: #1f2fb5;
    --band-dark: #1c1c1e;
    --band-mid: #3a3a3d;
    --steel-light: #e9ebee;
    --steel-mid: #b5b9bf;
    --steel-dark: #7c8087;
    --text-light: #ffffff;
  }
  * { box-sizing: border-box; margin: 0; padding: 0; }
  html, body {
    width: 1125px; height: 1200px; overflow: hidden;
    background: var(--paper);
    font-family: "Exo 2", "Arial", sans-serif;
  }
  .card {
    position: absolute; left: 162px;
    width: 800px; height: 457px; overflow: hidden;
    box-shadow: 0 2px 6px rgba(0,0,0,.18);
  }
  .card--front { top: 110px; background: var(--white); }
  .card--back {
    top: 640px;
    background: linear-gradient(180deg, var(--navy-deep) 0%, var(--navy) 100%);
  }

  /* Front: brand */
  .brand {
    position: absolute; left: 60px; top: 52px;
    display: flex; align-items: center; gap: 22px;
  }
  .brand__dot {
    width: 104px; height: 104px; border-radius: 50%;
    background: var(--brand-blue);
  }
  .brand__name {
    font-family: "Exo 2", sans-serif; font-weight: 800;
    color: var(--brand-blue); text-transform: uppercase; line-height: 1;
  }
  .brand__name .line-main { display: block; font-size: 58px; letter-spacing: 3px; }
  .brand__name .line-sub { display: block; font-size: 25px; letter-spacing: 4px; margin-top: 8px; }

  .slogan-band {
    position: absolute; left: 0; top: 218px; width: 702px; height: 34px;
    background: linear-gradient(180deg, var(--band-mid), var(--band-dark));
    color: var(--text-light);
    font-family: "Exo 2", sans-serif; font-weight: 500; font-size: 22px;
    padding-left: 61px; line-height: 34px;
  }
  .fitting {
    position: absolute;
    background: linear-gradient(180deg, var(--steel-mid) 0%, var(--steel-light) 35%, var(--steel-mid) 65%, var(--steel-dark) 100%);
    border-radius: 2px;
  }
  .fitting--slogan { left: 702px; top: 218px; width: 98px; height: 34px; }

  .contact-panel {
    position: absolute; left: 0; top: 252px; width: 800px; height: 205px;
    background: linear-gradient(180deg, var(--navy-deep) 0%, var(--navy) 100%);
    color: var(--text-light);
  }
  .hotline-icon { position: absolute; left: 56px; top: 38px; width: 74px; height: 74px; }
  .phone-number {
    position: absolute; left: 144px; top: 34px;
    font-weight: 700; font-size: 40px; letter-spacing: 1px;
  }
  .website {
    position: absolute; left: 144px; top: 83px;
    font-family: "Poppins", sans-serif; font-size: 18px;
  }
  .person { position: absolute; left: 485px; top: 34px; }
  .person__name { font-weight: 700; font-size: 26px; letter-spacing: .5px; text-transform: uppercase; }
  .person__role, .person__email, .person__address {
    font-family: "Poppins", sans-serif; font-size: 16px; line-height: 1.4;
  }
  .person__email { font-size: 17px; margin-top: 2px; }
  .person__address { margin-top: 8px; padding-left: 4px; }

  /* Back */
  .brand-plate {
    position: absolute; left: 356px; top: 229px; width: 418px; height: 48px;
    background: var(--white);
    display: flex; align-items: center; justify-content: center;
  }
  .brand-plate__name {
    font-family: "Exo 2", sans-serif; font-weight: 800; font-size: 25px;
    letter-spacing: 2px; color: var(--brand-blue); text-transform: uppercase;
  }
  .service-line {
    position: absolute; height: 26px;
    background: linear-gradient(180deg, var(--band-mid), var(--band-dark));
    clip-path: polygon(22px 0, 100% 0, 100% 100%, 0 100%);
    color: var(--text-light);
    font-family: "Poppins", sans-serif; font-size: 18px;
    text-align: right; padding-right: 10px; line-height: 26px;
  }
  .service-line--1 { left: 317px; top: 319px; width: 387px; }
  .service-line--2 { left: 289px; top: 353px; width: 415px; }
  .service-line--3 { left: 262px; top: 387px; width: 442px; }
  .fitting--line { left: 704px; width: 72px; height: 26px; }
  .fitting--l1 { top: 319px; }
  .fitting--l2 { top: 353px; }
  .fitting--l3 { top: 387px; }
</style>
</head>
<body>

<section class="card card--front" aria-label="Business card front">
  <div class="brand">
    <span class="brand__dot"></span>
    <p class="brand__name"><span class="line-main">Meridian</span><span class="line-sub">Hose and Fittings</span></p>
  </div>

  <p class="slogan-band">Industry chosen hose and fittings provider</p>
  <div class="fitting fitting--slogan" role="img" aria-label="Hydraulic hose fitting"></div>

  <div class="contact-panel">
    <svg class="hotline-icon" viewBox="0 0 74 74" aria-hidden="true">
      <path d="M22 10 C10 14 6 28 8 40 C10 52 16 62 24 66" fill="none" stroke="#fff" stroke-width="6" stroke-linecap="round"/>
      <rect x="14" y="6" width="12" height="14" rx="3" fill="#fff"/>
      <rect x="18" y="58" width="12" height="14" rx="3" fill="#fff"/>
      <path d="M34 10 A28 28 0 1 1 36 66" fill="none" stroke="#fff" stroke-width="4"/>
      <path d="M54 8 L62 14 L52 18 Z" fill="#fff"/>
      <text x="40" y="44" text-anchor="middle" fill="#fff" font-family="Exo 2, sans-serif" font-weight="700" font-size="17">24/7</text>
    </svg>
    <p class="phone-number">0400 123 456</p>
    <p class="website">www.meridianhose.com.au</p>

    <div class="person">
      <p class="person__name">Daniel Harper</p>
      <p class="person__role">President</p>
      <p class="person__email">info@meridianhose.com.au</p>
      <p class="person__address">1420 Wattle Street<br>Geelong, Victoria 3220</p>
    </div>
  </div>
</section>

<section class="card card--back" aria-label="Business card back">
  <div class="brand-plate">
    <p class="brand-plate__name">Meridian Hose and Fittings</p>
  </div>

  <p class="service-line service-line--1">24/7 on-site service</p>
  <div class="fitting fitting--line fitting--l1" role="img" aria-label="Hydraulic hose fitting"></div>
  <p class="service-line service-line--2">supply &amp; hose management</p>
  <div class="fitting fitting--line fitting--l2" role="img" aria-label="Hydraulic hose fitting"></div>
  <p class="service-line service-line--3">Experienced | independant | family owned</p>
  <div class="fitting fitting--line fitting--l3" role="img" aria-label="Hydraulic hose fitting"></div>
</section>

</body>
</html>
```